New minimal and cool business card

We have a brand new logo - we would like to use the logo on blue on the front of the card
The tagline is The share and lend circle (tm)
We would like information on the back of the card for individual(s)

Our font is Lato
Our colors are indicated in the attached identity guide which uses the old logo - we are de-emphasizing orange

Please prepare the artwork to meet the specs on this site
http://us.prinvo.com/products/velora/business-cards.html

Front: Logo and tagline on dark blue

Back: On white
Join Today
http://zentaro.co/join

```html
<!DOCTYPE html>
<html lang="en">
<head>
<meta charset="utf-8">
<title>Zentaro Business Card</title>
<link rel="stylesheet" href="https://fonts.googleapis.com/css2?family=Lato:wght@300;400&display=swap">
<style>
  :root {
    --backdrop: #e4e5e7;
    --card-navy: #2d4460;
    --card-white: #fbfbfa;
    --logo-silver: #c9ced4;
    --tagline-grey: #b4bdc8;
    --ink-dark: #2b2b2b;
    --ink-mid: #4a4a4a;
    --card-shadow: rgba(20, 28, 40, 0.18);
  }
  html, body {
    margin: 0;
    padding: 0;
    width: 1200px;
    height: 1200px;
    overflow: hidden;
    background: var(--backdrop);
    font-family: "Lato", sans-serif;
  }
  .canvas {
    width: 1200px;
    height: 1200px;
    display: flex;
    flex-direction: column;
    align-items: center;
    justify-content: center;
    gap: 60px;
  }
  .card {
    width: 840px;
    height: 480px;
    box-shadow: 0 6px 24px var(--card-shadow);
    display: flex;
    flex-direction: column;
    align-items: center;
    justify-content: flex-start;
    box-sizing: border-box;
  }
  .card--front {
    background: var(--card-navy);
    padding-top: 96px;
  }
  .card--back {
    background: var(--card-white);
    padding-top: 150px;
  }
  .brand-lockup {
    display: flex;
    flex-direction: column;
    align-items: flex-end;
  }
  .brand-name {
    font-weight: 400;
    font-size: 96px;
    line-height: 1;
    letter-spacing: 1px;
    color: var(--logo-silver);
  }
  .brand-stage {
    font-weight: 400;
    font-size: 16px;
    line-height: 1;
    letter-spacing: 9px;
    color: var(--logo-silver);
    margin-top: 4px;
    margin-right: -9px;
  }
  .tagline {
    font-weight: 300;
    font-size: 18px;
    line-height: 1.2;
    color: var(--tagline-grey);
    margin: 20px 0 0;
  }
  .call-to-action {
    font-weight: 300;
    font-size: 44px;
    line-height: 1.1;
    color: var(--ink-dark);
    margin: 0;
  }
  .join-url {
    font-weight: 300;
    font-size: 26px;
    line-height: 1.2;
    color: var(--ink-mid);
    margin-top: 10px;
  }
</style>
</head>
<body>
  <main class="canvas">
    <section class="card card--front" aria-label="Card front">
      <div class="brand-lockup">
        <span class="brand-name">zentaro</span>
        <span class="brand-stage">BETA</span>
      </div>
      <p class="tagline">The share and lend circle (tm)</p>
    </section>
    <section class="card card--back" aria-label="Card back">
      <h1 class="call-to-action">Join today</h1>
      <div class="join-url">http://zentaro.co/join</div>
    </section>
  </main>
</body>
</html>
```